Corporate Design für jur. Repetitorium
Extrem professionell, freundlich und hilfsbereit. Die Designs hatten stets eine sehr hohe Qualität und wurden, egal um welche Idee oder Variation es sich auch gehandelt hat, mehrfach ohne Beanstandung und nahezu umgehend modifiziert. Ich kann die Zusammenarbeit nur loben und hervorheben und gebe an dieser Stelle den sechsten Stern! Weiter so!
Zielgruppe
Wir sind ein jur. Repetitorium und bieten Individual- und Gruppenunterricht für Studenten an, die sich auf ihre Prüfungen vorbereiten. Unsere Zielgruppe liegt daher bei Studiumsanfängern und Fortgeschrittenen. Alter ca. 19 - 27. Primär visieren wir Studenten an, die bereit sind für kleinen Gruppen- sowie Individualunterricht etwas mehr zu zahlen. Wir sind ein international ausgerichtetes Unternehmen. Neben Studenten- bieten wir des weiteren auch jur. Weiterbildungskurse für fertige Anwälte an. Wichtig ist uns ein moderner und aufgeschlossener Auftritt, der sich von dem sehr langweiligen und konservativen Image gängiger Kanzleien und Repetitorien abhebt. Jung, modern und frisch wollen wir wirken da wir ein junges Team sind.
Aufgabenstellung
Wir wollen seriös aber nicht zu ernst wirken, professionell, persönlich, eine entspannte und effektive Lernatmosphäre bietend. Es soll ein gutes persönliches Gefühl entstehen, ein sorgenfreier aber leistungsorientierter Lernflair der sich von der normalen Lernumgebung abhebt. Auch unser Corporate Design soll diese Einstellung zeigen. Da wir mit modernen Medien wie Korvs , Quimbo Stylos, Beamer, Cloud und online Tutoring arbeiten, sollte dies auch im Design Ausdruck finden. Wir sind im Vergleich zu anderen Anbietern international aufgestellt, da wir sowohl das nationale deutsche Recht anbieten, aber auch europäisches Recht, sowie Rechtvergleichung mit andern Rechtssystemen. Dieses Konzept und die damit verbundene Internationalität, kann gerne im Design eingebracht werden. Sehr gut gefällt uns z.B. der Auftritt von Quimbo.
Gerne mit silber-, weißtönen, grau, platin:)

```html
<!DOCTYPE html>
<html lang="de">
<head>
<meta charset="utf-8">
<title>Briefbogen – KAVERO</title>
<link rel="stylesheet" href="https://fonts.googleapis.com/css2?family=Saira:wght@400;500&family=Open+Sans:wght@300;400;600&display=swap">
<style>
  :root {
    --ink: #333333;
    --muted: #555555;
    --frame: #6a6a6a;
    --green: #8cbf26;
    --mark-green: #5aa02c;
    --paper: #ffffff;
  }
  html, body {
    margin: 0;
    padding: 0;
    width: 1004px;
    height: 1200px;
    overflow: hidden;
    background: var(--paper);
  }
  .board {
    position: relative;
    width: 1004px;
    height: 1200px;
    font-family: "Saira", sans-serif;
    color: var(--ink);
  }
  .board-title {
    position: absolute;
    top: 0;
    left: 0;
    width: 1004px;
    margin: 0;
    text-align: center;
    font-size: 56px;
    font-weight: 400;
    letter-spacing: 1.5px;
    line-height: 60px;
  }
  .letterhead {
    position: absolute;
    left: 105px;
    top: 114px;
    width: 771px;
    height: 1084px;
    border: 1.5px solid var(--frame);
    box-sizing: border-box;
    background: var(--paper);
  }
  .sender-line {
    position: absolute;
    left: 84px;
    top: 172px;
    margin: 0;
    font-family: "Open Sans", sans-serif;
    font-size: 7.5px;
    color: var(--ink);
    white-space: nowrap;
  }
  .sender-line strong { font-weight: 600; }
  .brand {
    position: absolute;
    left: 540px;
    top: 262px;
    width: 226px;
    text-align: center;
  }
  .brand-name {
    display: inline-flex;
    align-items: center;
    gap: 8px;
    font-family: "Open Sans", sans-serif;
    font-weight: 300;
    font-size: 24px;
    letter-spacing: 0.5px;
    color: var(--ink);
    line-height: 28px;
  }
  .brand-dot {
    width: 10px;
    height: 10px;
    border-radius: 50%;
    background: var(--green);
  }
  .brand-tagline {
    margin: 2px 0 0;
    font-family: "Open Sans", sans-serif;
    font-size: 8px;
    color: var(--muted);
  }
  .fold-mark {
    position: absolute;
    left: -2px;
    width: 7px;
    height: 7px;
    background: var(--ink);
  }
  .fold-mark--top { top: 381px; }
  .fold-mark--middle { top: 538px; width: 9px; height: 9px; background: var(--mark-green); }
  .fold-mark--bottom { top: 764px; }
  .footer-brand {
    position: absolute;
    left: 237px;
    top: 955px;
    width: 300px;
    text-align: center;
    font-family: "Open Sans", sans-serif;
  }
  .footer-name {
    margin: 0;
    font-size: 14px;
    font-weight: 400;
    line-height: 16px;
    color: var(--ink);
  }
  .footer-tagline {
    margin: 0 0 10px;
    font-size: 6px;
    color: var(--muted);
  }
  .footer-address {
    margin: 0;
    font-size: 8px;
    font-weight: 600;
    line-height: 11px;
    color: var(--ink);
  }
  .footer-country {
    margin: 0;
    font-size: 6px;
    color: var(--muted);
  }
  .footer-web {
    position: absolute;
    left: 237px;
    top: 1040px;
    width: 300px;
    margin: 0;
    text-align: center;
    font-family: "Saira", sans-serif;
    font-size: 15px;
    line-height: 18px;
    font-weight: 500;
    letter-spacing: 0.5px;
    color: var(--green);
  }
  .footer-block {
    position: absolute;
    top: 1017px;
    margin: 0;
    font-size: 9.5px;
    line-height: 13.5px;
    color: var(--ink);
  }
  .footer-bank { left: 84px; }
  .footer-bank .label {
    display: inline-block;
    width: 22px;
    font-size: 6.5px;
    font-weight: 500;
  }
  .footer-registry {
    right: 84px;
    text-align: right;
  }
</style>
</head>
<body>
<main class="board">
  <h1 class="board-title">Briefbogen – abstrakter Paragraph</h1>

  <section class="letterhead">
    <p class="sender-line"><strong>KAVERO</strong> | Lindenweg 4 | 12345 Berlin | germany</p>

    <div class="brand">
      <div class="brand-name"><span class="brand-dot"></span>KAVERO</div>
      <p class="brand-tagline">Individual- &amp; gruppenrepetitorium</p>
    </div>

    <span class="fold-mark fold-mark--top"></span>
    <span class="fold-mark fold-mark--middle"></span>
    <span class="fold-mark fold-mark--bottom"></span>

    <div class="footer-brand">
      <p class="footer-name">KAVERO</p>
      <p class="footer-tagline">Individual- &amp; gruppenrepetitorium</p>
      <p class="footer-address">LINDENWEG 4<br>12345 BERLIN</p>
      <p class="footer-country">germany</p>
    </div>

    <p class="footer-block footer-bank">
      Bankverbindung<br>
      <span class="label">IBAN</span>DE89 7310 0000 5521 908 40<br>
      <span class="label">BIC</span>KVBXDEFFXXX
    </p>

    <p class="footer-web">www.kavero.de</p>

    <p class="footer-block footer-registry">
      Amtsgericht Berlin HRB 47219<br>
      USt-ID DE987654321<br>
      Steuernummer 321/456/78901
    </p>
  </section>
</main>
</body>
</html>
```